SUMMIT GATHERING 2021. August 20th -22nd.

The Hosts of the conference: Grace Tabernacle-Pastors Ron n Della ( Picture with two persons)

Guest Minister: Bishop Lucinda Okotieno. (Cedar Ridge Awakening)

Venue:
Sealand Gateway Lodgeview. 4817 North 239th Avenue Seattle, WA 98174.

Conference times.
Friday August 20th 6pm-8:30pm
Saturday August 21st. 6pm-8:30pm

Sunday August 22nd 10am-1pm
“ CHURCH RENEWAL GATHERING”

5pm-7:30pm
TWOFOLD SURGE GATHERING.

Target Market(s)

18-55

Industry/Entity Type

Religious/ Entertainment.

Requirements
Must have
• A highlight of the Relaunch service on Sunday August 22nd 5pm-7:30pm.
Nice to have
• Excellent ideas….

```html
<!DOCTYPE html>
<html lang="en">
<head>
<meta charset="utf-8">
<title>Church Renewal Gathering – Grace Tabernacle</title>
<link rel="stylesheet" href="https://fonts.googleapis.com/css2?family=Bebas+Neue&family=Oswald:wght@300;600&family=Asap+Condensed:wght@400&display=swap">
<style>
  :root {
    --black: #000000;
    --orange: #ffa700;
    --yellow: #ffff00;
    --white: #ffffff;
    --gold: #f2a516;
  }
  html, body {
    margin: 0;
    padding: 0;
    width: 1200px;
    height: 927px;
    overflow: hidden;
    background: var(--black);
  }
  .flyer {
    position: relative;
    width: 1200px;
    height: 927px;
    background: var(--black);
    font-family: "Bebas Neue", sans-serif;
  }
  .flyer-shapes {
    position: absolute;
    inset: 0;
  }
  .block {
    position: absolute;
    text-align: center;
    margin: 0;
  }
  .schedule {
    font-family: "Bebas Neue", sans-serif;
    font-size: 44px;
    line-height: 45px;
    color: var(--black);
    letter-spacing: 0.5px;
  }
  .schedule--sunday { left: 24px; width: 240px; top: 136px; }
  .schedule--evening { left: 920px; width: 256px; top: 136px; }

  .brand {
    position: absolute;
    left: 520px;
    width: 156px;
    top: 86px;
    display: flex;
    flex-direction: column;
    align-items: center;
    gap: 10px;
    font-family: "Oswald", sans-serif;
    font-weight: 600;
    font-size: 19px;
    line-height: 1;
    color: var(--gold);
    letter-spacing: 1px;
  }
  .brand-mark {
    width: 44px;
    height: 44px;
    background: var(--gold);
  }

  .headline {
    left: 330px;
    width: 536px;
    top: 196px;
    font-family: "Bebas Neue", sans-serif;
    font-size: 128px;
    line-height: 110px;
    color: var(--yellow);
  }

  .venue {
    left: 420px;
    width: 356px;
    top: 560px;
    font-family: "Asap Condensed", sans-serif;
    font-size: 21px;
    line-height: 36.5px;
    color: var(--white);
  }
  .venue p { margin: 0; }
  .venue .gap { height: 26px; }

  .host-label, .guest-label {
    font-family: "Asap Condensed", sans-serif;
    font-size: 27px;
    color: var(--white);
    top: 802px;
    line-height: 34px;
  }
  .host-label { left: 24px; width: 412px; }
  .guest-label { left: 850px; width: 275px; }

  .host-names, .guest-name {
    font-family: "Oswald", sans-serif;
    color: var(--orange);
    top: 842px;
    line-height: 34px;
    white-space: nowrap;
  }
  .host-names { left: 24px; width: 412px; font-size: 23px; font-weight: 300; }
  .host-names strong { font-weight: 600; }
  .guest-name { left: 820px; width: 335px; font-size: 25px; font-weight: 600; }
</style>
</head>
<body>
<main class="flyer">
  <svg class="flyer-shapes" width="1200" height="927" viewBox="0 0 1200 927" xmlns="http://www.w3.org/2000/svg">
    <defs>
      <linearGradient id="hostsTone" x1="0" y1="0" x2="1" y2="1">
        <stop offset="0" stop-color="#3a2a26"/>
        <stop offset="0.55" stop-color="#d9dde6"/>
        <stop offset="1" stop-color="#f2efee"/>
      </linearGradient>
      <linearGradient id="guestTone" x1="0" y1="0" x2="0" y2="1">
        <stop offset="0" stop-color="#3b2a22"/>
        <stop offset="0.55" stop-color="#6b4c3c"/>
        <stop offset="1" stop-color="#8a8a8a"/>
      </linearGradient>
    </defs>
    <rect class="frame" x="24" y="34" width="1152" height="859" fill="var(--orange)" stroke="var(--orange)" stroke-width="2"/>
    <polygon class="stripe-left" points="228,35 248,35 449,793 429,793" fill="var(--yellow)"/>
    <polygon class="center-panel" points="248,35 953,35 752,793 449,793" fill="var(--black)"/>
    <polygon class="stripe-right" points="953,35 973,35 772,793 752,793" fill="var(--yellow)"/>
    <path class="photo-hosts" role="img" aria-label="Photo of the hosts, Pastors Ron and Della"
          d="M26,528 Q40,372 118,356 Q200,350 212,420 Q250,382 300,392 Q340,420 345,520 Q370,610 420,690 L444,793 L26,793 Z"
          fill="url(#hostsTone)"/>
    <path class="photo-guest" role="img" aria-label="Photo of guest minister Bishop Lucinda Okotieno"
          d="M808,793 L826,680 Q850,640 880,620 Q870,560 880,470 Q905,380 980,378 Q1045,385 1048,470 Q1050,560 1045,600 Q1110,640 1168,690 L1176,793 Z"
          fill="url(#guestTone)"/>
    <rect class="footer-band" x="25" y="793" width="1150" height="99" fill="var(--black)"/>
  </svg>

  <h2 class="block schedule schedule--sunday">Sunday<br>August 22nd<br>10am-1pm</h2>

  <div class="brand">
    <span class="brand-mark"></span>
    <span class="brand-name">GRACE TABERNACLE</span>
  </div>

  <h2 class="block schedule schedule--evening">5pm-7:30pm<br>Twofold Surge<br>Gathering.</h2>

  <h1 class="block headline">Church<br>Renewal<br>Gathering</h1>

  <section class="block venue">
    <p>Venue:</p>
    <p>Sealand Gateway Lodgeview. 4817 North</p>
    <p>239th Avenue Seattle, WA 98174.</p>
    <div class="gap"></div>
    <p>Conference times.</p>
    <p>Friday August 20th 6pm-8:30pm</p>
    <p>Saturday August 21st. 6pm-8:30pm</p>
  </section>

  <p class="block host-label">The Hosts of the conference:</p>
  <p class="block host-names">GRACE TABERNACLE-PASTORS <strong>RON &amp; DELLA</strong></p>

  <p class="block guest-label">Guest Minister:</p>
  <p class="block guest-name">BISHOP LUCINDA OKOTIENO</p>
</main>
</body>
</html>
```